'The Willow Lantern Boutique' Ecommerce boutique (womens clothing) needs a business card design

Ecommerce boutique (womens clothing) needs a business card design, we need a business card that's fresh, innovative, clean design that matches our quality products and attracts quality suppliers as well as customers.
We aim to create a feel good shopping experience that goes past the point of sale.
Updates
Target Market(s)
Women 18-35, fashion forward, disposable income, unique.
Industry/Entity Type
Boutique
Font styles to use
Colors
Designer to choose colors to be used in the design.
Look and feel
Each slider illustrates characteristics of the customer's brand and the style your logo design should communicate.

```html
<!DOCTYPE html>
<html lang="en">
<head>
<meta charset="utf-8">
<title>The Willow Lantern Boutique – Business Card</title>
<link rel="stylesheet" href="https://fonts.googleapis.com/css2?family=Cormorant+Garamond:ital,wght@0,500;1,500&display=swap">
<style>
  :root {
    --backdrop: #e7e3de;
    --card-dark: #0b0b0b;
    --card-dark-pattern: #161616;
    --mint: #22b983;
    --mint-pattern: #3cc391;
    --band: #2dbd88;
    --ink-light: #ffffff;
    --ink-soft: #e9e9e9;
    --shadow: rgba(0,0,0,0.28);
  }
  * { box-sizing: border-box; margin: 0; padding: 0; }
  html, body {
    width: 1200px; height: 576px; overflow: hidden;
    background: var(--backdrop);
    font-family: "Cormorant Garamond", Georgia, serif;
  }
  .stage { position: relative; width: 1200px; height: 576px; }

  .card {
    position: absolute;
    width: 500px; height: 286px;
    border-radius: 3px;
    overflow: hidden;
    box-shadow: 0 10px 24px var(--shadow);
  }
  .card-pattern { position: absolute; inset: 0; }

  /* Front (dark) */
  .card-front { left: 70px; top: 70px; background: var(--card-dark); }
  .card-front .card-pattern {
    background: radial-gradient(ellipse at 60% 55%, var(--card-dark-pattern), var(--card-dark) 75%);
  }
  .brand-name {
    position: absolute;
    color: var(--ink-light);
    font-weight: 500;
    text-align: center;
    line-height: 1;
  }
  .brand-name .brand-main { display: block; font-size: 30px; }
  .brand-name .brand-sub { display: block; font-size: 17px; letter-spacing: 0.42em; margin-top: 4px; }
  .card-front .brand-name { left: 30px; top: 34px; }

  .holder {
    position: absolute; right: 34px; top: 30px;
    text-align: right; color: var(--ink-light); font-style: italic;
  }
  .holder-name { font-size: 21px; }
  .holder-role { font-size: 17px; margin-top: 2px; color: var(--ink-soft); }

  .contact-list { position: absolute; left: 0; top: 160px; list-style: none; }
  .contact-band {
    display: flex; align-items: center; gap: 16px;
    height: 30px; margin-bottom: 9px;
    padding-left: 12px;
    background: var(--band);
    color: var(--ink-light);
    font-style: italic; font-size: 18px; letter-spacing: 0.03em;
    white-space: nowrap;
  }
  .contact-band.phone { width: 205px; }
  .contact-band.email { width: 440px; }
  .contact-band.web { width: 450px; }
  .contact-icon { width: 18px; height: 18px; flex: none; }

  /* Back (mint) */
  .card-back { left: 630px; top: 210px; background: var(--mint); }
  .card-back .card-pattern {
    background: radial-gradient(ellipse at 50% 50%, var(--mint-pattern), var(--mint) 80%);
  }
  .card-back .brand-name {
    left: 0; right: 0; top: 110px;
  }
  .card-back .brand-main { font-size: 40px; }
  .card-back .brand-sub { font-size: 22px; }
</style>
</head>
<body>
<main class="stage">

  <section class="card card-front" aria-label="Business card front">
    <div class="card-pattern" role="img" aria-label="Faint dark floral vine pattern"></div>

    <div class="brand-name">
      <span class="brand-main">Willow Lantern</span>
      <span class="brand-sub">BOUTIQUE</span>
    </div>

    <div class="holder">
      <p class="holder-name">Maren Holloway</p>
      <p class="holder-role">Founder</p>
    </div>

    <ul class="contact-list">
      <li class="contact-band phone">
        <svg class="contact-icon" viewBox="0 0 24 24" aria-hidden="true"><path fill="#fff" d="M6.6 10.8a15 15 0 0 0 6.6 6.6l2.2-2.2c.3-.3.7-.4 1-.2 1.1.4 2.3.6 3.6.6.6 0 1 .4 1 1V20c0 .6-.4 1-1 1A17 17 0 0 1 3 4c0-.6.4-1 1-1h3.5c.6 0 1 .4 1 1 0 1.3.2 2.5.6 3.6.1.3 0 .7-.2 1z"/></svg>
        <span>0412 555 018</span>
      </li>
      <li class="contact-band email">
        <svg class="contact-icon" viewBox="0 0 24 24" aria-hidden="true"><rect x="2.5" y="5" width="19" height="14" fill="none" stroke="#fff" stroke-width="2"/><path d="M3 6l9 7 9-7" fill="none" stroke="#fff" stroke-width="2"/></svg>
        <span>maren@willowlanternboutique.com.au</span>
      </li>
      <li class="contact-band web">
        <svg class="contact-icon" viewBox="0 0 24 24" aria-hidden="true"><circle cx="12" cy="12" r="9" fill="none" stroke="#fff" stroke-width="2"/><path d="M3 12h18M12 3c3 3 3 15 0 18M12 3c-3 3-3 15 0 18" fill="none" stroke="#fff" stroke-width="1.5"/></svg>
        <span>www.thewillowlanternboutique.com</span>
      </li>
    </ul>
  </section>

  <section class="card card-back" aria-label="Business card back">
    <div class="card-pattern" role="img" aria-label="Light mint floral vine pattern"></div>
    <div class="brand-name">
      <span class="brand-main">Willow Lantern</span>
      <span class="brand-sub">BOUTIQUE</span>
    </div>
  </section>

</main>
</body>
</html>
```